Talverno Industrial Services Decontamination

We need a Brochure Design for a new company based in Jubail Eastern Region in Saudi Arabia. The name of our new Company is "Talverno Industrial Services Company", Our Industrial Services include liquid/dry vacuuming, hydro jetting and blasting, boiler cleaning, condenser and heat exchanger tube cleaning, Tank Cleaning, Decontamination, chemical cleaning, and pipe cleaning and removal etc.

We are dedicated to providing excellent service and fast turn around for completing projects on-time, within budget, and without incident.
Updates

I have uploaded the Logo, I am also putting a 40 US$ Participation Payment

Project Deadline Extended
Reason: Required more designs

Target Market(s)

Petrochemical Plants, Oil & Gas Companies, EPC Contractors etc.

Industry/Entity Type

It Company

Requirements
Must have
• Rich with high resolution pictures and Graphics. Designer has to provide these pictures and graphics. If there is extra charges for the pictures we will pay.

Good pictures for each project. Brochure should be very Informative and not boring. Should have highlight text, bubbled text etc.

The maximum pages should be from 4-6.

```html
<!DOCTYPE html>
<html lang="en">
<head>
<meta charset="utf-8">
<title>Talverno Industrial Services – Brochure Spread</title>
<link rel="stylesheet" href="https://fonts.googleapis.com/css2?family=Source+Sans+3:wght@400;600&display=swap">
<style>
  :root{
    --page-bg:#ffffff;
    --yellow:#f4d935;
    --yellow-ink:#8d89a6;
    --yellow-head:#8a86b0;
    --paper:#f7f7f7;
    --paper-2:#fbfbfb;
    --grey:#8f8f8f;
    --ink-grey:#7a7a7a;
    --ink-dark:#6a6a6a;
    --accent:#f5d33a;
    --white:#ffffff;
  }
  *{margin:0;padding:0;box-sizing:border-box}
  html,body{width:1200px;height:558px;overflow:hidden;background:var(--page-bg)}
  body{font-family:"Source Sans 3",Arial,sans-serif}
  .spread{position:absolute;left:30px;top:59px;width:1141px;height:440px;display:flex}
  .panel{position:relative;height:100%}
  .panel--decon{width:363px;background:var(--yellow);color:var(--yellow-ink)}
  .panel--degas{width:206px;background:var(--paper)}
  .panel--column{width:185px;background:var(--paper-2)}
  .panel--tank{width:387px;background:var(--grey);color:var(--white)}
  .folio{position:absolute;top:22px;font-size:7px;letter-spacing:.1px}
  .panel--decon .folio{left:41px;color:var(--yellow-ink)}
  .panel--tank .folio{right:48px;color:var(--accent)}
  .title{position:absolute;top:56px;font-weight:400;font-size:18px;letter-spacing:-.2px}
  .panel--decon .title{left:41px;color:var(--yellow-head)}
  .panel--degas .title{left:16px;color:var(--ink-grey)}
  .panel--tank .title{left:20px;color:var(--accent)}
  .block{position:absolute;font-size:6.6px;line-height:10.2px}
  .block h3{font-size:6.8px;font-weight:600;margin-bottom:1px}
  .block p{margin:0}
  .block + .block{}
  .gap{height:9px}
  .panel--decon .block h3{color:var(--yellow-head)}
  .panel--degas .block{color:var(--ink-grey)}
  .panel--degas .block h3{color:var(--ink-dark)}
  .panel--tank .block h3{color:var(--white)}
  .art{position:absolute}
  .art--decon{left:95px;top:225px;width:225px;height:203px;background:linear-gradient(180deg,#e7d640 0%,#9bb13a 70%,#3f7a2a 100%);border-radius:3px}
  .art--column{left:10px;top:104px;width:147px;height:260px;background:linear-gradient(180deg,#eef2f8 0%,#c9d6ea 60%,#3d6fd0 100%);border-radius:3px}
  .art--tank{left:173px;width:171px;border-radius:2px}
  .art--tank-1{top:91px;height:52px;background:linear-gradient(180deg,#b9b9b9,#2a2a2a)}
  .art--tank-2{top:168px;height:52px;background:linear-gradient(180deg,#c0c0c0,#3a3a3a)}
  .art--tank-3{top:245px;height:53px;background:linear-gradient(90deg,#3f8f3a,#a67c3a,#2f2f2f,#6bb04a)}
  .art--tank-4{top:311px;height:82px;background:linear-gradient(180deg,#b7c2c6,#5fb7c4)}
</style>
</head>
<body>
<main class="spread">

  <section class="panel panel--decon">
    <div class="folio">05 | Talverno Industrial Services Co.</div>
    <h2 class="title">Decontamination</h2>
    <div class="block" style="left:41px;top:102px;width:172px">
      <h3>Hydrocarbon Removal / Polymer Removal</h3>
      <p>To be used in heavily fouled systems to remove fouling prior to degassing</p>
      <p>Evaluate fouling type present in equipment</p>
      <p>Chemicals added to the solvent</p>
      <p>To be used in a hydrocarbon or Water solution (1-3%) to soften and Remove heavy hydrocarbon deposits</p>
      <p>Soften and fouling removal agent</p>
      <p>Apply heat during cleaning (65-850C)</p>
      <p>Strainers / Filter equipment must be considered</p>
      <p>HC solution could be sent to slop-oil facility, burned or processed</p>
    </div>
    <div class="block" style="left:221px;top:102px;width:135px">
      <h3>Recirculation Method ( Liquid Phase)</h3>
      <p>Cleaning &amp; degassing</p>
      <p>Recycle via overhead or Reflux</p>
      <p>Circulation to applied to Heat Exchangers</p>
      <div class="gap"></div>
      <h3>Once through Method</h3>
      <p>No Circulation (no loop possible)</p>
      <p>Non preferred method due to High costs</p>
    </div>
    <div class="art art--decon" role="img" aria-label="Process diagram of a column with recirculation loop, drum, pumps and valves"></div>
  </section>

  <section class="panel panel--degas">
    <h2 class="title">Degassing</h2>
    <div class="block" style="left:16px;top:102px;width:182px">
      <h3>Degassing</h3>
      <p>Absorbs both V/L HC by promoting a rapid emulsion in water to remove</p>
      <p>Penetrates deposits to lift off HC and absorb them</p>
      <p>Apply heat during degassing (65-850C)</p>
      <p>To be used in water solution (1-3%)</p>
      <p>To absorb light hydrocarbons (benzene,etc.) and to clean the surface of the equipment.</p>
      <p>Degassing can be performed I.C.W steaming</p>
      <div class="gap"></div>
      <h3>Steam Purge Method (Vapor Phase)</h3>
      <p>Degassing</p>
      <p>Saturated Steam</p>
      <p>Overhead sent to flare / drum</p>
      <p>Condensate / emulsion to be sent to tank for settling and disposing.</p>
      <p>Reduced amount of waste water to</p>
      <p>Be processed</p>
      <div class="gap"></div>
      <h3>Emulsion Breakers</h3>
      <p>The emulsion normally brakes on its own in 4-6 hours without any HC release into the atmosphere.</p>
      <p>Emulsion breaker might be needed when the emulsion does not break on it's own</p>
      <p>Emulsion breakers remain into the HC phase and minimizes effects of waste water facilities.</p>
    </div>
  </section>

  <section class="panel panel--column">
    <div class="art art--column" role="img" aria-label="Diagram of a steam-purged column venting to flare drum with condensate emulsion outlet"></div>
  </section>

  <section class="panel panel--tank">
    <div class="folio">Talverno Industrial Services Co. | 06</div>
    <h2 class="title">Tank Cleaning</h2>
    <div class="block" style="left:20px;top:102px;width:150px">
      <h3>Circulation Method</h3>
      <p>&nbsp;Add the cleaning solution to penetrate sludge</p>
      <p>Apply heat and recirculation</p>
    </div>
    <div class="block" style="left:20px;top:180px;width:150px">
      <p>Sludge tends to reach diluents on the top</p>
    </div>
    <div class="block" style="left:20px;top:247px;width:150px">
      <p>Cleaning Simulation</p>
    </div>
    <div class="block" style="left:20px;top:348px;width:150px">
      <h3>Degassing – Spray Method</h3>
      <p>From top or sides depending on deposit locations and configurations of manholes / access doors.</p>
    </div>
    <div class="art art--tank art--tank-1" role="img" aria-label="Tank diagram with cleaning solution circulating over sludge"></div>
    <div class="art art--tank art--tank-2" role="img" aria-label="Tank diagram showing sludge rising to diluent layer"></div>
    <div class="art art--tank art--tank-3" role="img" aria-label="Photo strip of cleaning simulation stages"></div>
    <div class="art art--tank art--tank-4" role="img" aria-label="Diagram of tank spray degassing with nozzle and piping"></div>
  </section>

</main>
</body>
</html>
```